Meurtre chez la Vern‘

“Vern’” is the informal nickname used inside the French police for the "Escouade Vernaleuse du Nord", an elite homicide unit. The apostrophe reflects spoken language and internal slang. The title Meurtre chez la Vern’ highlights the central irony of the novel: a murder committed inside the very place meant to investigate murders.
Summary
A woman’s body is found inside the offices of Paris’s elite homicide squad. As detectives investigate, they uncover buried cases, internal rivalries and institutional silence. The closer they get to the truth, the clearer it becomes: this crime was meant to stay hidden.
Keywords : Woman’s body, Police procedural, Murder inside the police, Elite homicide unit, Dark realism, 58 rue Bastelinou.
Size : 16 x 24 cm
Title : Meurtre chez la Vern'
Author : Lucien Maréchaux
Publisher : Editions Torvelle (at the bottom of the page)
Book

```html
<!DOCTYPE html>
<html lang="fr">
<head>
<meta charset="UTF-8">
<title>Meurtre chez la Vern' — Lucien Maréchaux</title>
<link href="https://fonts.googleapis.com/css2?family=Oswald:wght@500;600&family=Montserrat:wght@400&family=Open+Sans:wght@500&display=swap" rel="stylesheet">
<style>
  :root {
    --ink-deep: #07090a;
    --wall-dark: #1e2628;
    --wall-mid: #3a4644;
    --window-light: rgba(242, 228, 196, 0.85);
    --wall-light: rgba(214, 196, 156, 0.55);
    --floor-light: rgba(176, 128, 80, 0.6);
    --uniform: rgba(22, 40, 60, 0.95);
    --title: #ffffff;
    --author: #ffffff;
    --publisher: #8ea3ab;
  }
  html, body {
    margin: 0;
    padding: 0;
    width: 800px;
    height: 1200px;
    overflow: hidden;
    background: var(--ink-deep);
  }
  .cover {
    position: relative;
    width: 800px;
    height: 1200px;
    overflow: hidden;
  }
  .scene {
    position: absolute;
    inset: 0;
    background:
      radial-gradient(ellipse 95px 230px at 705px 200px, var(--window-light), rgba(200,170,120,0.25) 70%, transparent 100%),
      radial-gradient(ellipse 210px 150px at 170px 500px, var(--wall-light), transparent 85%),
      radial-gradient(ellipse 120px 110px at 320px 430px, rgba(200,184,146,0.35), transparent 85%),
      radial-gradient(ellipse 230px 60px at 130px 780px, var(--floor-light), transparent 90%),
      radial-gradient(ellipse 330px 170px at 480px 640px, var(--uniform), transparent 85%),
      radial-gradient(ellipse 220px 250px at 680px 760px, rgba(14,26,40,0.9), transparent 85%),
      linear-gradient(90deg, transparent 55%, rgba(10,12,13,0.55) 100%),
      linear-gradient(180deg, var(--wall-dark) 0%, var(--wall-mid) 30%, #2c3533 52%, #171c1c 70%, #0d1011 85%, var(--ink-deep) 100%);
  }
  .title {
    position: absolute;
    left: 0;
    right: 0;
    top: 58px;
    margin: 0;
    padding-left: 88px;
    font-family: 'Oswald', sans-serif;
    color: var(--title);
    text-shadow: 0 3px 12px rgba(0,0,0,0.5);
    line-height: 1;
  }
  .title-main {
    display: block;
    font-weight: 600;
    font-size: 180px;
    letter-spacing: -3px;
  }
  .title-sub {
    display: block;
    margin-top: 13px;
    padding-left: 14px;
    font-weight: 500;
    font-size: 125px;
    letter-spacing: -1px;
  }
  .author {
    position: absolute;
    left: 0;
    right: 0;
    top: 1030px;
    margin: 0;
    text-align: center;
    font-family: 'Montserrat', sans-serif;
    font-weight: 400;
    font-size: 36px;
    letter-spacing: 0.3em;
    color: var(--author);
  }
  .publisher {
    position: absolute;
    left: 0;
    right: 0;
    top: 1120px;
    margin: 0;
    text-align: center;
    font-family: 'Open Sans', sans-serif;
    font-weight: 500;
    font-size: 34px;
    color: var(--publisher);
  }
</style>
</head>
<body>
  <main class="cover">
    <div class="scene" role="img" aria-label="Photographie sombre : le corps d'une femme en uniforme de police étendu sur un parquet, lumière d'une fenêtre en haut à droite projetée sur le mur, insigne de police posé au sol"></div>
    <h1 class="title">
      <span class="title-main">MEURTRE</span>
      <span class="title-sub">chez la Vern'</span>
    </h1>
    <p class="author">LUCIEN MARÉCHAUX</p>
    <p class="publisher">EDITIONS TORVELLE</p>
  </main>
</body>
</html>
```